Coin collector banner ad for specialty insurance

We need a logo designed banner ad (multiple ads) to align with the coin collector market while incorporating color palette logo and call to action. Color palette of Fernholt. Dimension, images, example designs and color palette attached. The context should include 'Specialty Insurance for your coin collection' please refer to the designed examples

Target Market(s)

Coin collectors 30-65+ years of age primarily male

Industry/Entity Type

Insurance

Font styles to use
Sans Serif

Requirements
Must have
• color palette, logo, word mark, Call to Action, The words 'Specialty Insurance for your coin collection'
Nice to have
• Call to actions
Should not have
• ba

```html
<!DOCTYPE html>
<html lang="en">
<head>
<meta charset="utf-8">
<title>Fernholt – Coin Collection Banner Set</title>
<link rel="stylesheet" href="https://fonts.googleapis.com/css2?family=Source+Sans+3:wght@400;600;700;800&display=swap">
<style>
  :root {
    --canvas: #555555;
    --label: #f2f2f2;
    --brand-blue: #4b8fb8;
    --field-green: #7a8f3f;
    --paper: #ffffff;
    --ink: #1c1c1c;
    --navy: #1f2d5c;
    --logo-cyan: #1aa1dc;
    --arrow-cyan: #2bb5e8;
    --tagline: #f3e8cc;
  }
  html, body {
    margin: 0;
    width: 1200px;
    height: 1200px;
    overflow: hidden;
    background: var(--canvas);
    font-family: "Source Sans 3", "Source Sans Pro", sans-serif;
  }
  .sheet { position: relative; width: 1200px; height: 1200px; }
  .size-label {
    position: absolute;
    right: 90px;
    margin: 0;
    font-size: 22px;
    font-weight: 400;
    color: var(--label);
    letter-spacing: 0.3px;
    line-height: 1;
  }
  .banner {
    position: absolute;
    display: block;
    box-shadow: 0 18px 30px rgba(0,0,0,0.28);
  }
  .banner text { font-family: "Source Sans 3", "Source Sans Pro", sans-serif; }
  .headline { fill: var(--paper); font-weight: 600; letter-spacing: 1px; }
  .subline { fill: var(--ink); font-weight: 400; letter-spacing: 0.5px; }
  .brand-name { fill: var(--ink); font-weight: 700; letter-spacing: -1px; }
  .tagline { fill: var(--tagline); font-weight: 400; }
  .cta { fill: var(--navy); font-weight: 800; letter-spacing: 0.6px; }
  .bg-blue { fill: var(--brand-blue); }
  .bg-green { fill: var(--field-green); }
  .bg-paper { fill: var(--paper); }
  .logo-square { fill: var(--logo-cyan); }
  .cta-arrow { fill: var(--arrow-cyan); }
</style>
</head>
<body>
<main class="sheet">

  <!-- Landing page banner -->
  <h2 class="size-label" style="top:26px">GOV. LANDING PAGE</h2>
  <svg class="banner banner--landing" style="left:86px;top:50px" width="1024" height="280" viewBox="0 0 1280 350">
    <defs>
      <radialGradient id="silver" cx="40%" cy="35%" r="70%">
        <stop offset="0" stop-color="#f4f4f4"/><stop offset="0.6" stop-color="#c9c9c9"/><stop offset="1" stop-color="#8e8e8e"/>
      </radialGradient>
      <radialGradient id="gold" cx="40%" cy="35%" r="70%">
        <stop offset="0" stop-color="#e9cf7d"/><stop offset="0.6" stop-color="#c9a348"/><stop offset="1" stop-color="#8f6e22"/>
      </radialGradient>
      <radialGradient id="copper" cx="40%" cy="35%" r="70%">
        <stop offset="0" stop-color="#c9805a"/><stop offset="0.6" stop-color="#a35a39"/><stop offset="1" stop-color="#6e3722"/>
      </radialGradient>
      <clipPath id="clip-landing"><rect width="1280" height="350"/></clipPath>
    </defs>
    <g id="landing-art" clip-path="url(#clip-landing)">
      <rect class="bg-paper" width="1280" height="350"/>
      <polygon class="bg-green" points="560,0 1280,0 1280,350 550,350 478,87"/>
      <rect class="bg-blue" width="640" height="87"/>
      <g role="img" aria-label="Photograph of three collectible coins: a silver eagle, a gold double eagle and a copper large cent">
        <circle cx="1122" cy="82" r="150" fill="url(#copper)"/>
        <circle cx="692" cy="147" r="155" fill="url(#silver)"/>
        <circle cx="892" cy="134" r="176" fill="url(#gold)"/>
      </g>
      <polygon class="bg-blue" points="995,291 1280,225 1280,291"/>
      <polygon class="bg-paper" points="820,350 995,291 1280,291 1280,350"/>
      <text class="tagline" x="848" y="324" font-size="25" transform="rotate(-17 848 324)">PROTECTING YOUR PRIZED COLLECTION</text>
      <text class="cta" x="1009" y="330" font-size="28">GET INSURANCE</text>
      <path class="cta-arrow" d="M1240 311 l11 9 l-11 9 z M1252 311 l11 9 l-11 9 z"/>
      <text class="headline" x="38" y="62" font-size="48">SPECIALTY INSURANCE</text>
      <text class="subline" x="40" y="128" font-size="42">for your coin collection</text>
      <rect class="logo-square" x="41" y="226" width="88" height="88"/>
      <text class="brand-name" x="155" y="296" font-size="60">FERNHOLT</text>
    </g>
  </svg>

  <!-- Homepage large -->
  <h2 class="size-label" style="top:357px">GOV. HOMEPAGE LARGE</h2>
  <svg class="banner banner--large" style="left:366px;top:381px" width="744" height="204" viewBox="0 0 1280 350" preserveAspectRatio="none">
    <use href="#landing-art"/>
  </svg>

  <!-- Homepage medium -->
  <h2 class="size-label" style="top:615px">GOV. HOMEPAGE MEDIUM</h2>
  <svg class="banner banner--medium" style="left:406px;top:639px" width="704" height="272" viewBox="0 0 880 340">
    <defs><clipPath id="clip-medium"><rect width="880" height="340"/></clipPath></defs>
    <g clip-path="url(#clip-medium)">
      <rect class="bg-paper" width="880" height="340"/>
      <polygon class="bg-green" points="330,0 880,0 880,340 335,340 262,60"/>
      <rect class="bg-blue" width="450" height="60"/>
      <g role="img" aria-label="Photograph of three collectible coins: a silver eagle, a gold double eagle and a copper large cent">
        <circle cx="765" cy="101" r="138" fill="url(#copper)"/>
        <circle cx="424" cy="183" r="140" fill="url(#silver)"/>
        <circle cx="604" cy="141" r="134" fill="url(#gold)"/>
      </g>
      <polygon class="bg-blue" points="672,300 880,245 880,300"/>
      <polygon class="bg-paper" points="540,340 672,300 880,300 880,340"/>
      <text class="tagline" x="545" y="320" font-size="17" transform="rotate(-17 545 320)">PROTECTING YOUR PRIZED COLLECTION</text>
      <text class="cta" x="685" y="327" font-size="19">GET INSURANCE</text>
      <path class="cta-arrow" d="M846 314 l7 6 l-7 6 z M854 314 l7 6 l-7 6 z"/>
      <text class="headline" x="23" y="44" font-size="38">SPECIALTY INSURANCE</text>
      <text class="subline" x="254" y="92" font-size="33" text-anchor="end">for your coin</text>
      <text class="subline" x="254" y="130" font-size="33" text-anchor="end">collection</text>
      <rect class="logo-square" x="25" y="271" width="55" height="55"/>
      <text class="brand-name" x="96" y="313" font-size="38">FERNHOLT</text>
    </g>
  </svg>

  <!-- Homepage small -->
  <h2 class="size-label" style="top:929px">GOV. HOMEPAGE SMALL</h2>
  <svg class="banner banner--small" style="left:718px;top:953px" width="392" height="228" viewBox="0 0 490 285">
    <defs><clipPath id="clip-small"><rect width="490" height="285"/></clipPath></defs>
    <g clip-path="url(#clip-small)">
      <rect class="bg-paper" width="490" height="285"/>
      <polygon class="bg-green" points="200,0 490,0 490,285 195,285 150,43"/>
      <rect class="bg-blue" width="300" height="43"/>
      <g role="img" aria-label="Photograph of collectible coins: a silver eagle, a gold double eagle and a copper large cent">
        <circle cx="462" cy="69" r="95" fill="url(#copper)"/>
        <circle cx="272" cy="129" r="95" fill="url(#silver)"/>
        <circle cx="377" cy="109" r="95" fill="url(#gold)"/>
      </g>
      <polygon class="bg-blue" points="380,250 490,208 490,250"/>
      <polygon class="bg-paper" points="300,285 380,250 490,250 490,285"/>
      <text class="tagline" x="264" y="266" font-size="11" transform="rotate(-16 264 266)">PROTECTING YOUR PRIZED COLLECTION</text>
      <text class="cta" x="346" y="273" font-size="13">GET INSURANCE</text>
      <path class="cta-arrow" d="M467 264 l5 4 l-5 4 z M473 264 l5 4 l-5 4 z"/>
      <text class="headline" x="13" y="30" font-size="27">SPECIALTY INSURANCE</text>
      <text class="subline" x="147" y="73" font-size="24" text-anchor="end">for your coin</text>
      <text class="subline" x="147" y="101" font-size="24" text-anchor="end">collection</text>
      <rect class="logo-square" x="16" y="238" width="32" height="32"/>
      <text class="brand-name" x="58" y="262" font-size="23">FERNHOLT</text>
    </g>
  </svg>

</main>
</body>
</html>
```